Educational Software Company Seeking Event Postcard Design

We are looking for a postcard promoting an upcoming event. We would like to utilize the red, white and blue color scheme that you will see on the site at: http://buildingcrafters.campuswren.example/ksx. Gray can also be used. Please feel free to add some extra design elements. This postcard is targeting education operations professionals.

7th Annual Northern New England Plantworks Summit Gathering

When: February 27th -28th

Where: Portsmouth, New Hampshire

Call to action - Register Today: linkhop.example/PSG-Register

I have attached a word containing the text I'd like you to use and an example template. Some design elements will need to be added to the template

Red = bf1e2d
Blue = 0054a6

Target Market(s)

education operations professionals

Industry/Entity Type

Education

Requirements
Must have
• Plantworks Summit Gathering logo, name of conference, date, location, blue, red, white and gray seen on website:

Red = bf1e2d
Blue = 0054a6

When: February 27th -28th

```html
<!DOCTYPE html>
<html lang="en">
<head>
<meta charset="utf-8">
<title>Plantworks Summit Gathering Postcard</title>
<link href="https://fonts.googleapis.com/css2?family=Didact+Gothic&family=Questrial&family=Open+Sans:wght@600;700&display=swap" rel="stylesheet">
<style>
  :root {
    --red: #bf1e2d;
    --blue: #0054a6;
    --ink: #1d1d1f;
    --muted: #6a6a6a;
    --paper: #ffffff;
    --grey-top: #b9babd;
    --stage: #e7e7e7;
  }
  * { margin: 0; padding: 0; box-sizing: border-box; }
  html, body { width: 1200px; height: 1000px; overflow: hidden; }
  body { background: var(--stage); position: relative; font-family: "Questrial", sans-serif; color: var(--ink); }

  .card { position: absolute; background: var(--paper); overflow: hidden; }
  .card-front {
    left: 41px; top: 48px; width: 701px; height: 446px;
    background: linear-gradient(180deg, var(--grey-top) 0%, #e2e3e5 60%, var(--paper) 70%);
    text-align: center;
  }
  .card-back { left: 457px; top: 520px; width: 700px; height: 445px; }

  .event-title { font-size: 17px; font-weight: 400; white-space: nowrap; }
  .event-title sup, .event-date sup { font-size: 0.6em; line-height: 0; }
  .card-front .event-title { position: absolute; top: 38px; left: 0; right: 0; }

  .brand-mark { position: absolute; display: flex; align-items: center; justify-content: center; gap: 10px; }
  .brand-dot { width: 14px; height: 14px; border-radius: 50%; background: var(--blue); flex: none; }
  .brand-name { font-family: "Questrial", sans-serif; color: var(--red); line-height: 1.1; }
  .card-front .brand-mark { left: 230px; top: 90px; width: 240px; height: 130px; }
  .card-front .brand-name { font-size: 28px; text-align: center; }

  .event-date { font-size: 15px; white-space: nowrap; }
  .card-front .event-date { position: absolute; top: 228px; left: 0; right: 0; }

  .register-btn {
    position: absolute; display: flex; align-items: center; justify-content: center;
    background: var(--red); color: #fff; border-radius: 10px;
    border: 1px solid #e4a9a4; box-shadow: 0 1px 2px rgba(0,0,0,.35);
    font-family: "Open Sans", sans-serif; font-weight: 600; font-size: 13px; white-space: nowrap;
  }
  .card-front .register-btn { left: 189px; top: 270px; width: 323px; height: 21px; }

  .hosts-label { position: absolute; top: 338px; left: 0; right: 0; font-size: 14px; }
  .host-list { position: absolute; top: 362px; left: 260px; width: 180px; display: flex; justify-content: space-between; }
  .host { width: 54px; display: flex; flex-direction: column; align-items: center; gap: 4px; }
  .host-shape { width: 34px; height: 48px; background: #a9b3dc; }
  .host-shape.square { width: 48px; background: #dfe8dc; }
  .host-shape.circle { width: 36px; height: 36px; border-radius: 50%; background: #e9a22b; }
  .host-name { font-size: 6px; color: var(--blue); line-height: 1.1; }

  .card-back .brand-mark { left: 33px; top: 28px; width: 262px; height: 72px; justify-content: flex-start; }
  .card-back .brand-name { font-size: 24px; }
  .card-back .event-title { position: absolute; left: 27px; top: 136px; width: 400px; font-size: 12.5px; letter-spacing: -0.1px; font-family: "Open Sans", sans-serif; font-weight: 600; }
  .card-back .event-date { position: absolute; left: 27px; top: 163px; font-size: 12.5px; }
  .event-summary { position: absolute; left: 27px; top: 190px; width: 390px; font-family: "Didact Gothic", sans-serif; font-size: 12.5px; line-height: 18px; color: var(--muted); }
  .topic-list { position: absolute; left: 27px; top: 265px; list-style: none; font-family: "Didact Gothic", sans-serif; font-size: 12.5px; line-height: 18.5px; color: var(--muted); }
  .topic-list svg { width: 8px; height: 10px; margin-right: 6px; vertical-align: -1px; }
  .card-back .register-btn { left: 26px; top: 371px; width: 312px; height: 20px; }

  .mail-divider { position: absolute; left: 443px; top: 30px; width: 2px; height: 385px; background: var(--blue); }
  .return-address { position: absolute; left: 465px; top: 30px; width: 70px; text-align: center; }
  .return-name { font-family: "Open Sans", sans-serif; font-weight: 700; color: var(--blue); font-size: 11px; }
  .return-lines { font-size: 5px; color: var(--muted); line-height: 1.3; margin-top: 4px; }
</style>
</head>
<body>
  <section class="card card-front">
    <h1 class="event-title">7<sup>th</sup> Annual Northern New England Plantworks Summit Gathering</h1>
    <div class="brand-mark">
      <span class="brand-name">Plantworks Summit Gathering</span>
    </div>
    <p class="event-date">February 27<sup>th</sup>–28<sup>th</sup> in Portsmouth, New Hampshire</p>
    <div class="register-btn">Register Today: linkhop.example/PSG-Register</div>
    <p class="hosts-label">This conference is proudly hosted by:</p>
    <div class="host-list">
      <div class="host"><span class="host-shape"></span><span class="host-name">Granite Ledger Guild</span></div>
      <div class="host"><span class="host-shape square"></span><span class="host-name">Pinecoast Finance Circle</span></div>
      <div class="host"><span class="host-shape circle"></span><span class="host-name">CampusWren</span></div>
    </div>
  </section>

  <section class="card card-back">
    <div class="brand-mark">
      <span class="brand-dot"></span>
      <span class="brand-name">Plantworks Summit Gathering</span>
    </div>
    <h2 class="event-title">7<sup>th</sup> Annual Northern New England Plantworks Summit Gathering</h2>
    <p class="event-date">February 27<sup>th</sup>–28<sup>th</sup> in Portsmouth, New Hampshire</p>
    <p class="event-summary">This 2-day conference is packed with specialized networking, leadership and learning opportunities focused on facility and maintenance fundamentals for solving everyday challenges and achieving operational excellence. Some that will be discussed include:</p>
    <ul class="topic-list">
      <li><svg viewBox="0 0 8 10"><path d="M1 1l5 4-5 4" fill="none" stroke="#bf1e2d" stroke-width="2"/></svg>Facilities Management</li>
      <li><svg viewBox="0 0 8 10"><path d="M1 1l5 4-5 4" fill="none" stroke="#bf1e2d" stroke-width="2"/></svg>Energy Management</li>
      <li><svg viewBox="0 0 8 10"><path d="M1 1l5 4-5 4" fill="none" stroke="#bf1e2d" stroke-width="2"/></svg>Personnel Management</li>
      <li><svg viewBox="0 0 8 10"><path d="M1 1l5 4-5 4" fill="none" stroke="#bf1e2d" stroke-width="2"/></svg>School Safety</li>
      <li><svg viewBox="0 0 8 10"><path d="M1 1l5 4-5 4" fill="none" stroke="#bf1e2d" stroke-width="2"/></svg>Sustainability</li>
    </ul>
    <div class="register-btn">Register Today: linkhop.example/PSG-Register</div>
    <div class="mail-divider"></div>
    <div class="return-address">
      <div class="return-name">CampusWren</div>
      <div class="return-lines">4200 Lantern Ridge Way<br>Suite #210<br>Alder, NC 20000</div>
    </div>
  </section>
</body>
</html>
```